Update our OBGYN business card look and info

We are an OBGYN office. Our logo is nice but would like to "woman" part of the logo to be a darker color, to contrast with the flower that surrounds it. Maybe make our practice name Harbor Bloom Care Clinic more feminine. Our practice caters to women only. All providers and staff are female.

Target Market(s)

Females 16-65.

Industry/Entity Type

Business

Contact Information for Business Card

See attached upload. The ONLY CHANGE to the information is DELETE the name Dorothy Kemplin, Midwife and REPLACE with Greta Poundsworth, Midwife

Logo Text

Harbor Bloom Care Clinic Obstetrics & Gynecology

Font styles to use
Serif
Script

Colors
85cae6
0692cd
33a6d7
85abd2
f59195
eea4c8
cadf82
fac994
d3a5cc

```html
<!DOCTYPE html>
<html lang="en">
<head>
<meta charset="utf-8">
<title>Harbor Bloom Care Clinic – Business Card</title>
<link rel="stylesheet" href="https://fonts.googleapis.com/css2?family=Marcellus+SC&family=Open+Sans:wght@400;600;700&display=swap">
<style>
  :root {
    --page-bg: #e6e6e6;
    --card-white: #f7f7f7;
    --card-blue: #84c3d8;
    --brand-blue: #5cb8d9;
    --text-grey: #6b6b6b;
    --text-dark: #2f2f2f;
    --white: #ffffff;
  }
  * { box-sizing: border-box; margin: 0; padding: 0; }
  html, body {
    width: 1200px; height: 900px; overflow: hidden;
    background: var(--page-bg);
    font-family: "Open Sans", Arial, sans-serif;
  }
  .stage {
    width: 1200px; height: 900px;
    display: flex; align-items: center; justify-content: center; gap: 60px;
  }
  .card {
    width: 500px; height: 286px; position: relative;
    box-shadow: 0 6px 18px rgba(0,0,0,0.12);
  }
  .card--front { background: var(--card-white); padding: 30px 34px; }
  .card--back { background: var(--card-blue); display: flex; align-items: center; justify-content: center; }

  .brand { display: flex; align-items: center; gap: 12px; }
  .brand__dot { width: 34px; height: 34px; border-radius: 50%; background: var(--brand-blue); flex: none; }
  .brand__name {
    font-size: 13px; font-weight: 600; letter-spacing: 0.3px; text-transform: uppercase;
    color: var(--brand-blue); line-height: 1.2;
  }
  .brand__sub { font-size: 14px; font-weight: 700; color: var(--text-grey); line-height: 1.3; }

  .card--back .brand__dot { background: var(--white); width: 44px; height: 44px; }
  .card--back .brand__name { color: var(--white); font-size: 15px; }
  .card--back .brand__sub { color: var(--white); font-size: 17px; }

  .providers {
    list-style: none; margin-top: 22px;
    font-family: "Marcellus SC", Georgia, serif;
    font-size: 15px; line-height: 1.45; color: var(--brand-blue);
  }
  .contact {
    position: absolute; right: 30px; bottom: 26px;
    list-style: none; text-align: right;
    font-size: 11.5px; line-height: 1.5; color: var(--text-dark);
  }
  .contact li { display: flex; justify-content: flex-end; align-items: center; gap: 6px; }
  .contact svg { width: 10px; height: 10px; flex: none; }
  .contact .no-icon { padding-right: 16px; }
</style>
</head>
<body>
<main class="stage">
  <section class="card card--front" aria-label="Business card front">
    <div class="brand">
      <span class="brand__dot"></span>
      <div>
        <p class="brand__name">Harbor Bloom Care Clinic</p>
        <p class="brand__sub">Obstetrics &amp; Gynecology</p>
      </div>
    </div>
    <ul class="providers">
      <li>Marian Colbeck, MD</li>
      <li>Nadine Ashworth, MD</li>
      <li>Nadine Ashworth, MD</li>
      <li>Greta Poundsworth, Midwife</li>
      <li>Lorraine Featherby, Midwife</li>
    </ul>
    <ul class="contact">
      <li>555-014-2738
        <svg viewBox="0 0 10 10" aria-hidden="true"><path d="M2 1 L4 1 L4.6 3 L3.5 3.8 Q4.5 5.8 6.2 6.5 L7 5.4 L9 6 L9 8 Q5 9 2 5 Q1 3 2 1 Z" fill="var(--brand-blue)"/></svg>
      </li>
      <li>555-014-2153
        <svg viewBox="0 0 10 10" aria-hidden="true"><rect x="1.5" y="3" width="7" height="5" rx="1" fill="var(--brand-blue)"/><rect x="3" y="1" width="4" height="2.5" fill="var(--brand-blue)"/></svg>
      </li>
      <li>www.harborbloomcare.com
        <svg viewBox="0 0 10 10" aria-hidden="true"><circle cx="5" cy="5" r="4" fill="var(--brand-blue)"/></svg>
      </li>
      <li class="no-icon">418 Lantern Row Ste 2A</li>
      <li class="no-icon">Alder Falls, GA 31999-0142</li>
    </ul>
  </section>

  <section class="card card--back" aria-label="Business card back">
    <div class="brand">
      <span class="brand__dot"></span>
      <div>
        <p class="brand__name">Harbor Bloom Care Clinic</p>
        <p class="brand__sub">Obstetrics &amp; Gynecology</p>
      </div>
    </div>
  </section>
</main>
</body>
</html>
```